Change logo on company documents

I want to change the logo on all company documents and change them company name that is written in certain places in the text.

Target Market(s)

Construction/Residential Home Remodeling

Colors

Designer to choose colors to be used in the design.

```html
<!DOCTYPE html>
<html lang="en">
<head>
<meta charset="utf-8">
<title>Harlow Builders – Company Documents</title>
<link href="https://fonts.googleapis.com/css2?family=Open+Sans:ital,wght@0,400;0,600;0,700;1,400;1,600&display=swap" rel="stylesheet">
<style>
:root{
  --backdrop:#a5a5a5;
  --paper:#ffffff;
  --ink:#1c1c1c;
  --muted:#4a4a4a;
  --rule:#555555;
  --frame:#7a7a7a;
  --accent:#e2572a;
}
*{box-sizing:border-box;margin:0;padding:0}
html,body{width:1200px;height:1200px;overflow:hidden;background:var(--backdrop)}
body{position:relative;font-family:"Open Sans",Arial,sans-serif;color:var(--ink)}
.page{position:absolute;background:var(--paper);overflow:hidden}
.page-frame{position:absolute;inset:14px 15px;border:0.8px solid var(--frame);padding:16px 24px;overflow:hidden}
.brand{display:flex;align-items:center;gap:5px}
.brand-dot{width:22px;height:22px;border-radius:50%;background:var(--ink);flex:none}
.brand-name{font-weight:600;font-size:12px;letter-spacing:.3px;line-height:1}
.address{text-align:right;font-size:5.8px;line-height:1.45;letter-spacing:.5px}
.head{display:flex;justify-content:space-between;align-items:flex-start}
.doc-title{text-align:center;font-weight:600;letter-spacing:1.4px;font-size:11.5px}
.line{display:inline-block;border-bottom:0.6px solid var(--rule);vertical-align:bottom}
/* filing a claim */
.claim{left:70px;top:90px;width:391px;height:507px}
.claim .page-frame{padding:17px 27px}
.claim .doc-title{margin:30px 0 20px}
.claim ol{font-size:6.2px;line-height:1.75;padding-left:12px}
.claim li{margin-bottom:14px;padding-left:4px}
.field{display:flex;gap:3px;margin:7px 0 0 34px;width:210px}
.field .line{flex:1;height:7px}
/* agreement pages */
.agreement,.notice{top:90px;width:312px;height:513px}
.agreement{left:497px}
.notice{left:818px}
.agreement .page-frame,.notice .page-frame{inset:12px 12px;padding:12px 18px}
.agreement .brand-dot{width:18px;height:18px}
.agreement .brand-name{font-size:10px}
.agreement .address{font-size:4.5px;letter-spacing:.2px}
.agreement .doc-title{font-size:8.5px;letter-spacing:.2px;margin:18px 0 10px}
.small{font-size:3.9px;line-height:1.55}
.small b{font-weight:700}
.small p{margin-bottom:4px}
.opening{font-weight:600;font-size:3.9px;line-height:2.2}
.sigs{margin-top:14px}
.sig{display:flex;border-top:0.6px solid var(--rule);margin-top:14px;padding-top:2px;font-size:3.8px}
.sig span{width:55%}
.pnum{position:absolute;right:22px;bottom:30px;font-size:4px}
.lien{color:var(--accent);font-style:italic;text-align:center;font-size:3.9px;margin-top:14px}
.notice h2{text-align:center;font-size:8.5px;font-weight:600;margin:12px 0 8px}
/* bottom row */
.certificate{left:70px;top:644px;width:359px;height:465px}
.change{left:461px;top:644px;width:360px;height:465px}
.proposal{left:843px;top:644px;width:283px;height:465px}
.certificate .page-frame,.change .page-frame{padding:16px 23px}
.certificate .doc-title,.change .doc-title{margin:26px 0 30px;font-size:10.5px}
.body-text{font-size:5.3px;line-height:1.6}
.pair{display:flex;justify-content:space-between}
.pair .slot{width:46%;border-top:0.6px solid var(--rule);padding-top:2px;font-size:4.8px}
.scope-box{border:0.6px solid var(--rule);height:64px;margin:6px 0 10px}
/* proposal */
.proposal .page-frame{inset:11px 11px;padding:12px 12px}
.proposal .brand-dot{width:17px;height:17px}
.proposal .brand-name{font-size:9px}
.proposal .address{font-size:4.2px;letter-spacing:.2px}
.prop-title{display:flex;justify-content:space-between;align-items:flex-end;margin-top:14px}
.prop-title h1{font-size:7.5px;font-weight:600;letter-spacing:.6px}
.tag{background:var(--accent);color:#fff;font-weight:700;font-size:3.7px;padding:1px 2px}
.meta{display:grid;grid-template-columns:36px 40px;border:0.5px solid var(--rule)}
.meta div{height:6px;border-bottom:0.5px solid var(--rule)}
.prop-grid{display:flex;justify-content:space-between;margin-top:6px}
.box{border:0.5px solid var(--rule)}
.section{border:0.5px solid var(--rule);margin-top:8px}
.section .tag{display:block}
.row{padding:2px 3px;border-bottom:0.5px solid var(--rule);font-size:3.7px;line-height:1.45}
.row:last-child{border-bottom:none}
.row ol{padding-left:10px}
.note{color:var(--accent);font-style:italic;font-size:3.7px;text-align:center;margin-top:10px}
</style>
</head>
<body>

<section class="page claim">
  <div class="page-frame">
    <header class="head">
      <div class="brand"><span class="brand-dot"></span><span class="brand-name">Harlow Builders</span></div>
      <div class="address">400 CYPRESS ROW<br>SUITE 210 #118<br>RIVERTON, LA 70990<br>P:555.014.2200<br>F:555.014.2201</div>
    </header>
    <h1 class="doc-title">FILING A CLAIM</h1>
    <ol>
      <li>Call your Insurance Company to set up the claim. Your date of loss is the following;<br>date: <span class="line" style="width:90px"></span></li>
      <li>When you call in your claim, you will be given a claim number and be assigned an adjuster. Record this information below. Please make sure to ask for your adjuster's first and last name.
        <div class="field">Claim Number:<span class="line"></span></div>
        <div class="field">Adjuster's Name:<span class="line"></span></div>
        <div class="field">Contact:<span class="line"></span></div>
      </li>
      <li>Typically, the adjuster will call back in 3-5 business days to schedule an inspection. Once they do so, give them my name and number and ask them to contact me to schedule an inspection. Make sure they know you want your contractor present for the adjustment.</li>
      <li>When the adjuster gives you a date and time for the inspection, record the information below and contact me immediately afterword so I can prepare for the adjustment.
        <div class="field">Inspection Date:<span class="line" style="flex:none;width:62px"></span>&nbsp;&nbsp;&nbsp;&nbsp;&nbsp;&nbsp;&nbsp;&nbsp;Time:<span class="line"></span></div>
      </li>
      <li>The only way to make sure you are fairly represented during the inspection is to make sure I am present. Please contact me as soon as you get this information so I can be at your home to represent you.
        <div class="field">Claims Specialist:<span class="line"></span></div>
        <div class="field">Contact:<span class="line"></span></div>
      </li>
    </ol>
  </div>
</section>

<section class="page agreement">
  <div class="page-frame">
    <header class="head">
      <div class="brand"><span class="brand-dot"></span><span class="brand-name">Harlow Builders</span></div>
      <div class="address">1180 Delta Ave.<br>RIVERTON, LA 70991<br>P: 555.014.2210<br>F: 555.014.2211</div>
    </header>
    <h1 class="doc-title">CONSTRUCTION AGREEMENT</h1>
    <p class="opening">On this date <span class="line" style="width:120px"></span>, let it be known that the homeowner(s) <span class="line" style="width:150px"></span>, [Homeowner], of the property located at <span class="line" style="width:145px"></span> and Harlow Builders, otherwise known as, [Harlow], located at 1180 Delta Ave, Riverton, LA 70991 have entered into a contract to undergo building and or repairs specified on the proposal estimate supplied to the homeowner on <span class="line" style="width:60px"></span><br><span style="margin-left:170px">Total $ <span class="line" style="width:60px"></span></span></p>
    <div style="border-top:.6px solid var(--rule);margin:18px 0 6px"></div>
    <div class="small">
      <p><b>SECTION 1. ACKOWLEDGEMENT</b><br>1.1 Harlow is an independent contractor licensed and insured in the state of Louisiana and specializes in residential construction. Harlow acts on its own behalf and is not affiliated nor represents any insurance company or any other company. The owners acknowledge that it is their preference to do business with Harlow.</p>
      <p><b>SECTION 2. PAYMENT</b><br>2.1 Now therefore, the Homeowner hereby agrees as follows: The contract amount for work to be completed by Harlow will be determined by the pre agreed upon pricing in the provided proposal estimate.<br>2.2 A deposit of 50% of the contract amount will be given to Ostrel before any work begins. The second payment of the balance of the contract amount will be due to Ostrel upon completion of the job.<br>2.3 Payments shall either be mailed directly to Harlow's main office or hand-delivered to a Harlow representative only. The Client is personally responsible for any and all costs, charges, deductible, or depreciation not covered by insurance (if applicable).</p>
      <p><b>SECTION 3. INSURANCE SUPPLEMENTS (If Job is an In Insurance Job)</b><br>3.1 All supplements requested by Ostrel on behalf of the insured for additional damages discovered are to be paid by the property owner's insurance company, and will be given to the insured, once approved, and the insured will forward all supplemental funds to Harlow for supplemental work performed.<br>3.2 The insured hereby agree to have all work stated on the insurance supplemental loss sheet started or scheduled within 15 days of receiving the funds supplied by the insurance company.</p>
      <p><b>SECTION 4. AUTHORIZATION</b><br>4.1 I authorize Ostrel to supply information regarding the claim to my Insurance Company, and to make a full report of all work done by them.<br>4.2 In the event that Harlow is not allowed to perform its recommended procedures, I agree to release and hold Harlow harmless and indemnify Ostrel against any claims or actions that may result from such incomplete procedures.</p>
      <p style="font-weight:600;margin-top:8px">THIS SUBCONTRACT AGREEMENT IS ACKNOWLEDGED AND EXECUTED AS OF THE DATE SET FORTH ABOVE BY:</p>
    </div>
    <div class="sigs">
      <div class="sig"><span>Homeowner Signature</span>Date</div>
      <div class="sig"><span>Homeowner Signature</span>Date</div>
      <div class="sig"><span>Harlow Signature</span>Date</div>
    </div>
  </div>
  <span class="pnum">1</span>
</section>

<section class="page notice">
  <div class="page-frame">
    <p class="lien">Federal law requires that we give you the following notice of lien rights afforded to persons or companies furnishing labor or materials for the improvement of real property.</p>
    <h2>NOTICE</h2>
    <div class="small">
      <p><b>NOTICE OF CANCELLATION – YOU, THE BUYER, MAY CANCEL THIS PURCHASE ANY TIME PRIOR TO MIDNIGHT OF THE THIRD BUSINESS DAY AFTER THE DATE OF THIS PURCHASE IN WRITING.</b></p>
      <p><b>THE CONTRACT ON THE FACE HEREOF AND ANY AGREEMENT MADE PURSUANT THERETO BETWEEN THE "COMPANY" AND THE CUSTOMER(S) WILL BE SUBJECT TO ALL APPROPRIATE LAWS, REGULATIONS AND ORDINANCES, AND TO THE FOLLOWING SPECIAL TERMS AND CONDITIONS.</b></p>
      <p>1. It is agreed that the amount of the contract shall be the amount equal to value as stated on the Proposal.</p>
      <p>2. Our company has the right to order excess material. These materials will not be charged above the agreed upon price. All excess materials belong to our company.</p>
      <p>3. Additional labor and materials needed beyond the original scope of repairs shall be paid directly to the company and stated in the form of a change order.</p>
      <p>4. All material is guaranteed to be as specified. All work is to be completed in a workman-like manner according to standard practices. Any alterations or deviation from above specifications involving extra costs will be executed only upon written orders. All subcontractors carry Workmen's Compensation Insurance.</p>
      <p>5. This agreement constitutes the entire agreement between the parties. It may be changed only by written instrument signed by both parties.</p>
      <p>6. If any provision of this agreement should be held to be invalid or unenforceable, the validity of the remaining provisions shall not be affected thereby.</p>
      <p>7. Any representation or communication not written in this contract are agreed to be immaterial and do not survive its execution.</p>
      <p>8. If the Customer cancels this contract later than three (3) days from execution, but prior to the commencement of work, Customer shall pay to the Company twenty-five percent (25%) of the contract price as reasonable and just compensation for said cancellation.</p>
      <p>9. All accepted proposals are subject to approval of our Credit Department and Management.</p>
      <p>10. The Company is not responsible for any damage, pre-existing or future construction defects caused by storms or lack of maintenance during the period of the warranty.</p>
      <p>11. Should default be made in payment of this contract, interest charges shall be added at a rate of eight percent per annum (8% PER ANNUM) with a minimum charge of $2.00 per month.</p>
      <p>12. The above conditions shall be considered a part of this contract when the work is approved and will be paid for by the Insurance Company if applicable, or the homeowner.</p>
      <p>13. Homeowners agreement to the contingency statement, attached to this agreement, shall be considered a part of this contract.</p>
      <p>14. The dollar amount of the contract is the amount agreed upon by the homeowner plus any upgrades agreed to in writing and made part of this agreement or any change orders / insurance supplements.</p>
      <p>15. The final payment in full shall not be held up while waiting for the city to inspect the work. The company agrees to meet or exceed all city inspection requirements.</p>
    </div>
  </div>
  <span class="pnum">2</span>
</section>

<section class="page certificate">
  <div class="page-frame">
    <header class="head">
      <div class="brand"><span class="brand-dot"></span><span class="brand-name">Harlow Builders</span></div>
      <div class="address">400 CYPRESS ROW<br>SUITE 210 #118<br>RIVERTON, LA 70990<br>P: 555.014.2200<br>F: 555.014.2201</div>
    </header>
    <h1 class="doc-title">CERTIFICATE OF COMPLETION</h1>
    <div class="pair" style="margin-bottom:26px"><div class="slot">Homeowner</div><div class="slot">Completion Date</div></div>
    <p class="body-text">I/We hereby certify that all necessary repairs as outlined in the contract between Ostrel Roofing and <span class="line" style="width:105px"></span> located at <span class="line" style="width:150px"></span> have been completed in a satisfactory manner and all liens will be waived upon final payment for labor and materials.</p>
    <p class="body-text" style="margin-top:8px">All contractors, subcontractors and suppliers who have provided labor or materials in connection with the repairs to the property have been paid in full or will be paid from the final invoice proceeds.</p>
    <div class="pair" style="margin-top:80px"><div class="slot">Client</div><div class="slot">Harlow Builders</div></div>
    <div class="pair" style="margin-top:24px"><div class="slot">Date</div><div class="slot">Date</div></div>
  </div>
</section>

<section class="page change">
  <div class="page-frame">
    <header class="head">
      <div class="brand"><span class="brand-dot"></span><span class="brand-name">Harlow Builders</span></div>
      <div class="address">400 CYPRESS ROW<br>SUITE 210 #118<br>RIVERTON, LA 70990<br>P: 555.014.2200<br>F: 555.014.2201</div>
    </header>
    <h1 class="doc-title">CHANGE ORDER</h1>
    <div class="body-text" style="display:flex;justify-content:space-between"><span>Job Name: <span class="line" style="width:132px"></span></span><span>Date: <span class="line" style="width:76px"></span></span></div>
    <div class="body-text" style="display:flex;justify-content:space-between;margin-top:6px"><span>Job Location: <span class="line" style="width:125px"></span></span><span>Terms: <u>&nbsp;Due Upon Receipt&nbsp;&nbsp;&nbsp;&nbsp;&nbsp;&nbsp;</u></span></div>
    <p class="body-text" style="font-style:italic;font-weight:600;margin-top:14px">The following work/upgrades outlined below are changes to the scope specified on the original contract and/ or Insurance Loss Sheet. The homeowner(s) acknowledges they are responsible for these additional costs.</p>
    <div class="scope-box"></div>
    <p class="body-text" style="text-align:right;font-weight:600">Total Cost: <span class="line" style="width:76px"></span></p>
    <p class="body-text" style="margin-top:22px">By signing below the homeowner approves the additional work and/or upgrades and costs outlined above and agrees that payment for this change order is due upon signing of this agreement.</p>
    <div class="pair" style="margin-top:30px"><div class="slot">Homeowner</div><div class="slot">Harlow Builders</div></div>
    <div class="pair" style="margin-top:24px"><div class="slot">Date</div><div class="slot">Date</div></div>
  </div>
</section>

<section class="page proposal">
  <div class="page-frame">
    <header class="head">
      <div class="brand"><span class="brand-dot"></span><span class="brand-name">Harlow Builders</span></div>
      <div class="address">400 CYPRESS ROW<br>SUITE 210 #118<br>RIVERTON, LA 70990<br>P: 555.014.2200<br>F: 555.014.2201</div>
    </header>
    <div class="prop-title">
      <h1>ROOFING PROPOSAL</h1>
      <div class="meta"><div class="tag">PROPOSAL #:</div><div></div><div class="tag">DATE:</div><div></div></div>
    </div>
    <div class="prop-grid">
      <div class="box" style="width:93px;height:35px"><div class="tag">PROPOSAL FOR:</div></div>
      <div class="meta" style="grid-template-columns:44px 76px">
        <div class="tag">PROJECT/JOB:</div><div></div>
        <div class="tag">REPRESENTATIVE:</div><div></div>
        <div class="tag">EMAIL:</div><div></div>
        <div class="tag">CONTACT:</div><div></div>
        <div class="tag">DATE OF LOSS:</div><div></div>
      </div>
    </div>
    <div class="section">
      <span class="tag">DESCRIPTION</span>
      <div class="row" style="font-weight:600;width:147px;border-right:.5px solid var(--rule)">Scope of the proposed repairs are based on the estimate provided by the homeowner's insurance carrier:</div>
      <div class="row"><b>SCOPE OF THE PROPOSED REPAIRS INCLUDE:</b>
        <ol>
          <li>Remove existing hip and ridge capping.</li>
          <li>Remove existing roofing system.</li>
          <li>Inspect for any rotten or damaged decking and replace.</li>
          <li>Install Ice and Water Shield in valleys.</li>
          <li>Apply Ice and Water shield to all penetrations.</li>
          <li>Install synthetic underlayment.</li>
          <li>Remove and Replace drip edge around the perimeter of roof.</li>
          <li>Install starter shingles around the perimeter of the roof.</li>
          <li>Install <span class="line" style="width:70px"></span>, 6 nails per shingle.</li>
          <li>Replace all roofing pipe jacks with 3 in 1 aluminum base pipe jack.</li>
          <li>Replace Hip and Ridge capping.</li>
          <li>Replace necessary vents and caps.</li>
          <li>Remove debris from the job site.</li>
        </ol>
      </div>
      <div class="row"><b>PAYMENT SCHEDULE IS AS FOLLOWS:</b><br>&nbsp;&nbsp;• 30% &nbsp;Due upon acceptance of contract to begin work<br>&nbsp;&nbsp;• 70% &nbsp;Due Upon Completion of Work<br>Any rotten or damaged sheeting found while removing shingles will be replaced as needed at an additional cost of $125.00 per sheet. Ostrel Builders will not be responsible for any hidden or pre-existing conditions. A Two Year workmanship warranty is included on all repair work. Any additional changes or upgrades will be made by change orders signed by both parties.</div>
      <div class="row" style="font-weight:600">We propose herby to furnish labor and material - complete in accordance with above specifications, for the sum of: <span style="margin-left:20px">$</span></div>
    </div>
    <p class="row" style="border:none;padding:4px 0">All material is guaranteed to be as specified. All work to be completed in a workmanlike manner according to standard practices. Any alteration or deviation from above specifications involving extra costs will be executed only upon written orders. We are not responsible for any damaged landscaping. Our workers are fully covered by workman's compensation insurance.</p>
    <div class="pair" style="margin-top:16px"><div class="slot" style="font-size:3.7px">Homeowner</div><div class="slot" style="font-size:3.7px">Harlow Builders</div></div>
    <div class="pair" style="margin-top:10px"><div class="slot" style="font-size:3.7px">Date</div><div class="slot" style="font-size:3.7px">Date</div></div>
    <p class="note">Note: This proposal may be withdrawn by us if not accepted within 30 days.</p>
  </div>
</section>

</body>
</html>
```